Real Estate Marketing Company Needs 1 Page 8.5x11 Price List Flyer Design

We need a 1 page 8.5in x 11in price list flyer that is intended for drop off at local offices. This is intended to show all the services we offer including pricing to potential new clients. It should be separated into sections for the different services we offer. I'd also like some photos and our Logo on the list to make it look nice so its not all text. Try to incorporate the logo colors in the design.

Industry/Entity Type

Real Estate

Requirements
Must have
• Price List
• Photos
• Logo
• website address

```html
<!DOCTYPE html>
<html lang="en">
<head>
<meta charset="utf-8">
<title>Keystone Lens Studio – Price List</title>
<link href="https://fonts.googleapis.com/css2?family=Roboto:ital,wght@0,300;0,400;0,500;0,700;1,700&display=swap" rel="stylesheet">
<style>
:root{
  --stage:#2e2d2e;
  --ink:#070707;
  --paper:#ffffff;
  --red:#a8222a;
  --red-band:#a71f25;
  --text:#f2f2f2;
  --muted:#d6d6d6;
  --ring:#14292b;
}
*{box-sizing:border-box;margin:0;padding:0}
html,body{width:1200px;height:979px;overflow:hidden;background:var(--stage);font-family:'Roboto',Arial,sans-serif}
.canvas{position:relative;width:1200px;height:979px}

/* Front page */
.front{position:absolute;left:44px;top:147px;width:542px;height:698px;background:var(--ink);overflow:hidden}
.front__header{position:absolute;left:0;top:0;width:542px;height:196px;background:var(--paper);text-align:center}
.brand__dot{position:absolute;left:238px;top:50px;width:66px;height:66px;border-radius:50%;background:var(--ink)}
.brand__name{position:absolute;left:0;right:0;top:124px;font-size:22px;font-weight:500;letter-spacing:1px;color:var(--ink)}
.front__hero{position:absolute;left:0;top:196px;width:542px;height:237px;
  background:linear-gradient(180deg,#2f4a2a 0%,#4f7a3a 40%,#6fa7b8 70%,#3c8cb0 100%)}
.bubble{position:absolute;border-radius:50%;border:12px solid var(--ring)}
.bubble--aerial{left:44px;top:398px;width:146px;height:146px;background:linear-gradient(160deg,#5d7d3e,#2f4d27)}
.bubble--estate{left:160px;top:362px;width:226px;height:226px;background:linear-gradient(180deg,#6b9ed6 0%,#c7b08a 45%,#8d6d4c 100%)}
.bubble--brick{left:362px;top:400px;width:146px;height:146px;background:linear-gradient(180deg,#c58fb0 0%,#6b3d3e 55%,#d9d4da 100%)}
.front__tagline{position:absolute;left:0;right:0;top:609px;text-align:center;color:var(--red);font-size:14px;letter-spacing:5px}
.front__contact{position:absolute;left:0;right:0;top:643px;text-align:center;color:var(--muted);font-size:12px;line-height:15px}
.front__contact b,.back__contact b{color:#fff;font-weight:500}

/* Back page */
.back{position:absolute;left:614px;top:145px;width:544px;height:700px;background:var(--ink)}
.strip{position:absolute;top:46px;height:95px}
.strip--pool{left:0;width:118px;background:linear-gradient(180deg,#7fa2c9,#b99f7a 60%,#4c8aa8)}
.strip--hall{left:118px;width:148px;background:linear-gradient(180deg,#b7ab98,#e6e0d6 50%,#6b6155)}
.strip--porch{left:266px;width:135px;background:linear-gradient(180deg,#4e7a34,#d8d2c6 50%,#7a5a3a)}
.strip--living{left:401px;width:143px;background:linear-gradient(180deg,#c9b79a,#8a6a44 60%,#4a3322)}
.menu{position:absolute;left:28px;top:162px;width:500px;color:var(--text)}
.menu h2{color:var(--red);font-size:18px;font-weight:500;letter-spacing:.5px;line-height:20px;margin-bottom:4px}
.menu p{font-size:15px;font-weight:300;line-height:19px;letter-spacing:.3px}
.menu p b{font-weight:700}
.section{margin-bottom:15px}
.note{font-style:italic;font-weight:700!important;margin-top:4px}
.section--extras h2{font-size:15.5px;margin-bottom:2px}
.section--extras p{font-size:13px;line-height:16.5px}
.section--extras small{font-size:10.5px}
.floorplan{position:absolute;left:334px;top:266px;width:143px;height:184px;background:linear-gradient(180deg,#ffffff,#eef0f2)}
.back__band{position:absolute;left:0;top:633px;width:544px;height:67px;background:var(--red-band)}
.back__contact{position:absolute;left:0;right:0;top:645px;text-align:center;color:#f1e4e4;font-size:13.5px;line-height:17px;letter-spacing:.2px}
</style>
</head>
<body>
<main class="canvas">
  <section class="front">
    <header class="front__header">
      <span class="brand__dot"></span>
      <div class="brand__name">KEYSTONE LENS STUDIO</div>
    </header>
    <div class="front__hero" role="img" aria-label="Landscaped backyard with swimming pool, hot tub and white pool house"></div>
    <div class="bubble bubble--aerial" role="img" aria-label="Aerial view of a home surrounded by forest"></div>
    <div class="bubble bubble--brick" role="img" aria-label="Brick house at twilight with snow"></div>
    <div class="bubble bubble--estate" role="img" aria-label="Stone estate home with patio chairs and pool"></div>
    <p class="front__tagline">PRESENTATION IS EVERYTHING</p>
    <p class="front__contact">For more information or to book a shoot please visit our<br>website: <b>www.KeystoneLensStudio.com</b> or call <b>Dana at 555-014-2287</b></p>
  </section>

  <section class="back">
    <div class="strip strip--pool" role="img" aria-label="Mansion exterior with pool deck"></div>
    <div class="strip strip--hall" role="img" aria-label="Bright two-storey living room"></div>
    <div class="strip strip--porch" role="img" aria-label="Screened porch with wicker furniture"></div>
    <div class="strip strip--living" role="img" aria-label="Living room with chandelier and fireplace"></div>

    <div class="menu">
      <div class="section">
        <h2>PACKAGE PRICING</h2>
        <p>Silver Package: 15 Photos + Floor Plan (3,500 sqft) - <b>$225</b></p>
        <p>Gold Package: 25 Photos + Floor Plan (4,500 sqft) - <b>$300</b></p>
        <p>Platinum Package: 35 Photos + Floor Plan (5,500 sqft) - <b>$375</b></p>
      </div>
      <div class="section">
        <h2>PHOTOGRAPHY ONLY</h2>
        <p>15 Photo Bundle: <b>$100</b></p>
        <p>25 Photo Bundle: <b>$150</b></p>
        <p>35 Photo Bundle: <b>$200</b></p>
      </div>
      <div class="section">
        <h2>FLOOR PLANS</h2>
        <p>Floor Plan (3,500 sqft) - <b>$150</b></p>
        <p>Floor Plan (4,500 sqft) - <b>$175</b></p>
        <p>Floor Plan (5,500 sqft) - <b>$200</b></p>
        <p>*<b>$25</b> per additional 500sqft</p>
        <p class="note">**Complex floor plans are priced individually regardless of sqft</p>
      </div>
      <div class="section section--extras">
        <h2>ADDITIONAL SERVICES</h2>
        <p>Aerial Photos: 3-6 Photos - <b>$200</b> <small>($75 if combined with another package)</small></p>
        <p>Aerial Video: (1-3 min video) - <b>$375</b></p>
        <p>Branded Video Tour w/ Aerial Video: <small>(2-4 min video of property)</small> - <b>$800-$1300</b><br><small>(voiceover optional, call for details)</small></p>
        <p>Twilight Photos: 3-6 Photos - <b>$225</b></p>
        <p>Luxury Package: <b>$2,000</b> <small>(includes all services listed)</small></p>
      </div>
    </div>

    <div class="floorplan" role="img" aria-label="Two-storey floor plan drawing"></div>

    <div class="back__band"></div>
    <p class="back__contact">For more information or to book a shoot please visit our<br>website: <b>www.KeystoneLensStudio.com</b> or call <b>Dana at 555-014-2287</b></p>
  </section>
</main>
</body>
</html>
```